A Healthy BRAX Louisiana- TOVL Conference Poster

LA Carewell is presenting at the TOVL conference. The TOVL is a annual meeting for State, Federal and private sector individuals to provide opportunities for the exchange of ideas related to Carewell systems and heath policy affected by those systems. Louisiana will be presenting on their LaBRAX Program . A poster with the information in the PowerPoint is needed. The first slide shows a draft of organization. The wording on slides two and three should be displayed in a visually appealing infographic. The charts should coordinate with the overall design. We would like to see the Louisiana state capital building incorporated.

Font styles to use
Sans Serif

Colors

Designer to choose colors to be used in the design.

Requirements
Must have
• Visually appealing infographics and charts
Nice to have
• Incorporate the capital building, incorporate the LaBRAX logo (on first slide)

```html
<!DOCTYPE html>
<html lang="en">
<head>
<meta charset="utf-8">
<title>A Healthy BRAX Louisiana</title>
<link rel="stylesheet" href="https://fonts.googleapis.com/css2?family=Crimson+Pro:wght@400;500;600&display=swap">
<style>
  :root {
    --ink: #ffffff;
    --obstacle: #ff5151;
    --obstacle-deep: #c8141a;
    --solution: #2fe02a;
    --solution-deep: #16a514;
    --sky-dark: #160f24;
    --sky-mid: #4d2f6e;
    --sky-light: #9b86c8;
    --sky-blue: #6fb0e6;
  }
  * { box-sizing: border-box; margin: 0; padding: 0; }
  html, body { width: 1200px; height: 604px; overflow: hidden; background: var(--sky-dark); }
  body { font-family: "Crimson Pro", Georgia, serif; color: var(--ink); }
  .poster { position: relative; width: 1200px; height: 604px; overflow: hidden; }

  .backdrop {
    position: absolute; inset: 0;
    background:
      radial-gradient(ellipse 260px 420px at 600px 330px, rgba(120,95,160,.55), transparent 70%),
      linear-gradient(100deg, #120c1f 0%, #2d1c46 25%, #5a3a80 55%, #8a74bb 78%, var(--sky-blue) 100%);
  }
  .backdrop::after {
    content: ""; position: absolute; inset: 0;
    background: linear-gradient(180deg, transparent 55%, rgba(20,12,30,.75) 85%, #0d0914 100%);
  }

  .title {
    position: absolute; left: 58px; top: 38px;
    font-size: 46px; font-weight: 500; letter-spacing: .3px; white-space: nowrap;
  }
  .intro {
    position: absolute; left: 682px; top: 22px; width: 500px;
    font-size: 11px; line-height: 15px; text-align: justify;
  }
  .intro p + p { margin-top: 15px; }

  .pillar {
    position: absolute; top: 120px; width: 59px; height: 281px; border-radius: 30px;
    display: flex; align-items: center; justify-content: center;
  }
  .pillar span {
    font-size: 30px; letter-spacing: 1px; white-space: nowrap; font-weight: 500;
  }
  .pillar--obstacles { left: 477px; background: linear-gradient(180deg, var(--obstacle), var(--obstacle-deep)); }
  .pillar--obstacles span { transform: rotate(90deg); }
  .pillar--solutions { left: 655px; background: linear-gradient(180deg, var(--solution), var(--solution-deep)); }
  .pillar--solutions span { transform: rotate(-90deg); }

  .card { position: absolute; width: 173px; height: 95px; }
  .card__frame {
    position: absolute; inset: 0; border: 1px solid; border-bottom: none; border-radius: 14px 14px 0 0;
    -webkit-mask-image: linear-gradient(180deg, #000 30%, transparent 100%);
    mask-image: linear-gradient(180deg, #000 30%, transparent 100%);
  }
  .card--obstacle .card__frame { border-color: var(--obstacle); }
  .card--solution .card__frame { border-color: var(--solution); }
  .card__label {
    position: absolute; top: -16px; left: 50%; transform: translateX(-50%);
    border-radius: 14px; text-align: center; font-size: 13px; line-height: 14px;
    padding: 2px 8px; letter-spacing: .3px; white-space: nowrap;
  }
  .card--obstacle .card__label { background: var(--obstacle); }
  .card--solution .card__label { background: var(--solution-deep); background: #25cf20; }
  .card__text {
    position: absolute; left: 7px; right: 7px; font-size: 9px; line-height: 11.7px; text-align: justify;
  }

  .charts { position: absolute; inset: 0; pointer-events: none; }
  .charts text { font-family: "Crimson Pro", Georgia, serif; }

  .brand {
    position: absolute; left: 13px; top: 545px; width: 83px; height: 37px;
    background: #fff; border-radius: 5px;
    display: flex; align-items: center; justify-content: center; gap: 5px;
    font-size: 16px; color: #2d4f9a; font-weight: 500;
  }
  .brand__mark { width: 10px; height: 10px; background: #6aa84f; }
</style>
</head>
<body>
<div class="poster">
  <div class="backdrop" role="img" aria-label="Dusk photograph of the Louisiana State Capitol tower rising above trees under a purple sky"></div>

  <h1 class="title">A Healthy BRAX Louisiana</h1>

  <div class="intro">
    <p>Louisiana Benefit Relief Assistance Exchange (LaBRAX) program allows for Carewell to pay the premium costs of member’s private health insurance when cost effective for the State.</p>
    <p>To increase program participation the State is implementing strategic changes to increase enrollment by 95%, resulting in an $11.2M cost savings to the State by the end of SFY23.</p>
  </div>

  <div class="pillar pillar--obstacles"><span>THE OBSTACLES</span></div>
  <div class="pillar pillar--solutions"><span>THE SOLUTIONS</span></div>

  <section class="card card--obstacle" style="left:56px;top:160px;">
    <div class="card__frame"></div>
    <div class="card__label" style="top:-16px;">LACK OF<br>PUBLIC KNOWLEDGE</div>
    <p class="card__text" style="top:40px;">Members are unaware that this program exists or find it hard to believe that Carewell will pay for their private health insurance.</p>
  </section>

  <section class="card card--obstacle" style="left:284px;top:164px;">
    <div class="card__frame"></div>
    <div class="card__label" style="top:-15px;">BUDGET CONSTRAINTS</div>
    <p class="card__text" style="top:14px;">Due to a budgetary shortfall the LaBRAX program was discontinued on Dec 2015. By ending the program, all members were forced to cover their private insurance premiums, or switch to Carewell.</p>
  </section>

  <section class="card card--obstacle" style="left:53px;top:302px;">
    <div class="card__frame"></div>
    <div class="card__label" style="top:-15px;">LACK OF<br>PARTICIPATION</div>
    <p class="card__text" style="top:37px;">Cost effectiveness formula is too restrictive excluding a large portion of the viable population, including waiver, Fee for Service (FFS) members and the individual insurance market.</p>
  </section>

  <section class="card card--obstacle" style="left:285px;top:302px;">
    <div class="card__frame"></div>
    <div class="card__label" style="top:-13px;">CROWD OUT</div>
    <p class="card__text" style="top:32px;">Crowd out occurs when members choose public insurance in lieu of available private health insurance.</p>
  </section>

  <section class="card card--solution" style="left:761px;top:161px;">
    <div class="card__frame"></div>
    <div class="card__label" style="top:-16px;">PROGRAM RESTORED</div>
    <p class="card__text" style="top:33px;">LaBRAX was reinstated in April 2017, restoring LCH’s focus on promoting employer-sponsored insurance.</p>
  </section>

  <section class="card card--solution" style="left:989px;top:161px;">
    <div class="card__frame"></div>
    <div class="card__label" style="top:-16px;font-size:12px;">INCREASE AWARENESS<br>&amp; PUBLIC KNOWLEDGE</div>
    <p class="card__text" style="top:27px;">LCH has contracted a marketing firm to develop a comprehensive marketing and outreach strategy aimed at engaging providers, employers, insurance companies and members.</p>
  </section>

  <section class="card card--solution" style="left:759px;top:300px;">
    <div class="card__frame"></div>
    <div class="card__label" style="top:-15px;">INCREASE<br>PARTICIPATION</div>
    <p class="card__text" style="top:25px;">Refinement of the cost effectiveness formula increased the pool of members eligible for the program, including waiver, Fee for Service (FFS) members and the individual insurance market.</p>
  </section>

  <section class="card card--solution" style="left:991px;top:300px;">
    <div class="card__frame"></div>
    <div class="card__label" style="top:-17px;">DATA &amp; ANALYTICS</div>
    <p class="card__text" style="top:32px;">The use of data mining identifies individuals and populations to be targeted for program outreach.</p>
  </section>

  <svg class="charts" viewBox="0 0 1920 967" width="1200" height="604" aria-hidden="true">
    <g class="chart chart--before" fill="#ff5151" stroke="#ff5151">
      <line x1="312" y1="883" x2="798" y2="883" stroke-width="3"/>
      <g stroke-width="2" stroke-dasharray="9 6">
        <line x1="457" y1="813" x2="457" y2="883"/>
        <line x1="557" y1="745" x2="557" y2="883"/>
        <line x1="657" y1="673" x2="657" y2="883"/>
      </g>
      <polyline points="358,883 457,813 557,745 657,673 756,883" fill="none" stroke-width="3"/>
      <g stroke="none">
        <circle cx="358" cy="883" r="4.5"/><circle cx="457" cy="813" r="4.5"/><circle cx="557" cy="745" r="4.5"/>
        <circle cx="657" cy="673" r="4.5"/><circle cx="756" cy="883" r="4.5"/>
      </g>
      <line x1="664" y1="680" x2="702" y2="708" stroke-width="1.2"/>
      <line x1="703" y1="709" x2="788" y2="709" stroke-width="1.2"/>
      <g stroke="none" font-size="17" text-anchor="middle" font-weight="600">
        <text x="358" y="872">0</text><text x="462" y="802">500</text><text x="557" y="733">1000</text>
        <text x="656" y="664">1500</text><text x="756" y="873">0</text>
        <text x="705" y="707" text-anchor="start" font-size="15" font-weight="400">Funding Lost</text>
        <text x="355" y="909">FY12</text><text x="452" y="909">FY13</text><text x="556" y="909">FY14</text>
        <text x="656" y="909">FY15</text><text x="753" y="909">FY16</text>
        <text x="571" y="943" font-size="19" font-weight="500">LaBRAX Participants Chart</text>
      </g>
    </g>

    <g class="chart chart--after" fill="#2fe02a" stroke="#2fe02a">
      <line x1="1220" y1="878" x2="1687" y2="878" stroke-width="3"/>
      <g stroke-width="1" stroke-dasharray="4 4" stroke="#c9f5c6">
        <line x1="1320" y1="816" x2="1320" y2="878"/><line x1="1401" y1="796" x2="1401" y2="878"/>
        <line x1="1482" y1="756" x2="1482" y2="878"/><line x1="1564" y1="718" x2="1564" y2="878"/>
        <line x1="1645" y1="672" x2="1645" y2="878"/>
      </g>
      <polyline points="1238,878 1320,816 1401,796 1482,756 1564,718 1645,672" fill="none" stroke-width="3"/>
      <g stroke="none">
        <circle cx="1238" cy="878" r="4.5"/><circle cx="1320" cy="878" r="4"/><circle cx="1401" cy="878" r="4"/>
        <circle cx="1482" cy="878" r="4"/><circle cx="1564" cy="878" r="4"/><circle cx="1645" cy="878" r="4"/>
        <circle cx="1320" cy="816" r="4.5"/><circle cx="1401" cy="796" r="4.5"/><circle cx="1482" cy="756" r="4.5"/>
        <circle cx="1564" cy="718" r="4.5"/><circle cx="1645" cy="672" r="4.5"/>
      </g>
      <g stroke-width="1.2">
        <polyline points="1092,832 1225,832 1238,878" fill="none"/>
        <polyline points="1242,771 1298,771 1318,814" fill="none"/>
        <polyline points="1237,720 1298,720 1399,794" fill="none"/>
        <polyline points="1478,849 1416,849 1403,800" fill="none"/>
      </g>
      <g stroke="none" font-size="15" text-anchor="middle">
        <text x="1240" y="858">0</text><text x="1331" y="806">435</text><text x="1402" y="782">566</text>
        <text x="1484" y="743">848</text><text x="1563" y="708">1103</text><text x="1650" y="653">1434</text>
        <g text-anchor="start" font-size="16">
          <text x="1092" y="829">Program Restored</text>
          <text x="1242" y="768">Current</text>
          <text x="1185" y="696">Marketing Firm</text>
          <text x="1237" y="717">Engaged</text>
          <text x="1416" y="825">Formula</text>
          <text x="1416" y="846">Refined</text>
        </g>
        <g font-size="16" font-weight="600">
          <text x="1240" y="906">FY17</text><text x="1320" y="906">FY19</text><text x="1407" y="906">FY20</text>
          <text x="1485" y="906">FY21</text><text x="1565" y="906">FY22</text><text x="1646" y="906">FY23</text>
        </g>
        <text x="1466" y="943" font-size="19" font-weight="500">LaBRAX Participants Chart</text>
      </g>
    </g>
  </svg>

  <div class="brand"><span class="brand__mark"></span>LaBRAX</div>
</div>
</body>
</html>
```